I need a business card design for a new company that will be doing consulting work around issues of cultural competency, and diversity and inclusion. I would like the design to be crisp and clear with bold but conservative colors and incorporate shades of blue

Target Market(s)

Small businesses, schools, non-profits

Industry/Entity Type

Consulting

Font styles to use
Serif
Sans Serif

Colors
0c5ba6
6b449b
3276b5
0292cd

Requirements
Must have
• A Morrow Venture (name of company)
• Lemlem Tavish
• CEO
• lemlem@amorrowventure.com
• (215)483-2756

```html
<!DOCTYPE html>
<html lang="en">
<head>
<meta charset="utf-8">
<title>A Morrow Venture — Business Card</title>
<link rel="stylesheet" href="https://fonts.googleapis.com/css2?family=Barlow:wght@500;700&family=Open+Sans:wght@400&family=Arimo:wght@400&display=swap">
<style>
  :root {
    --brand-blue: #0c5ba6;
    --brand-purple: #6b449b;
    --mid-blue: #3276b5;
    --sky-blue: #0292cd;
    --soft-grey: #a7a9ac;
    --ink: #1a1a1a;
    --paper: #ffffff;
  }
  html, body {
    margin: 0;
    padding: 0;
    width: 1200px;
    height: 686px;
    overflow: hidden;
    background: var(--paper);
  }
  .card {
    position: relative;
    width: 1200px;
    height: 686px;
    overflow: hidden;
    background: var(--paper);
  }
  .edge-bar {
    position: absolute;
    left: 0;
    width: 9px;
  }
  .edge-bar--top { top: 0; height: 345px; background: var(--brand-purple); }
  .edge-bar--bottom { top: 345px; height: 341px; background: var(--sky-blue); }

  .globe-art {
    position: absolute;
    left: 800px;
    top: -148px;
    width: 982px;
    height: 982px;
    border-radius: 50%;
    background: linear-gradient(90deg, var(--brand-blue) 0%, var(--mid-blue) 30%, var(--brand-purple) 62%);
  }

  .wordmark {
    position: absolute;
    left: 71px;
    top: 84px;
    display: flex;
    align-items: center;
    gap: 16px;
  }
  .wordmark__square {
    width: 22px;
    height: 22px;
    background: var(--sky-blue);
  }
  .wordmark__name {
    font-family: "Barlow", sans-serif;
    font-weight: 700;
    font-size: 44px;
    line-height: 1.1;
    color: var(--brand-blue);
    margin: 0;
  }

  .person {
    position: absolute;
    left: 71px;
    top: 348px;
  }
  .person__name {
    margin: 0;
    font-family: "Barlow", sans-serif;
    font-size: 56px;
    line-height: 1;
    letter-spacing: 4px;
  }
  .person__first { color: var(--brand-blue); font-weight: 700; }
  .person__last { color: var(--soft-grey); font-weight: 500; margin-left: 10px; }
  .person__title {
    margin: 10px 0 0 0;
    font-family: "Arimo", sans-serif;
    font-size: 35px;
    line-height: 1;
    color: var(--ink);
  }

  .contact {
    position: absolute;
    left: 71px;
    top: 496px;
    list-style: none;
    margin: 0;
    padding: 0;
  }
  .contact__item {
    display: flex;
    align-items: center;
    height: 60px;
    font-family: "Open Sans", sans-serif;
    font-size: 43px;
    color: var(--ink);
  }
  .contact__icon {
    width: 44px;
    height: 32px;
    margin-right: 16px;
    flex: none;
  }
</style>
</head>
<body>
<div class="card">
  <div class="edge-bar edge-bar--top"></div>
  <div class="edge-bar edge-bar--bottom"></div>

  <div class="globe-art" role="img" aria-label="Globe illustration showing the continents in a blue-to-purple gradient"></div>

  <div class="wordmark">
    <span class="wordmark__square"></span>
    <p class="wordmark__name">A Morrow<br>Venture</p>
  </div>

  <div class="person">
    <h1 class="person__name"><span class="person__first">Lemlem</span><span class="person__last">Tavish</span></h1>
    <p class="person__title">CEO</p>
  </div>

  <ul class="contact">
    <li class="contact__item">
      <svg class="contact__icon" viewBox="0 0 44 32" aria-hidden="true">
        <rect x="2" y="4" width="40" height="25" fill="none" stroke="#0292cd" stroke-width="3"/>
        <polyline points="2,4 22,19 42,4" fill="none" stroke="#0292cd" stroke-width="3"/>
        <line x1="2" y1="29" x2="17" y2="15" stroke="#0292cd" stroke-width="3"/>
        <line x1="42" y1="29" x2="27" y2="15" stroke="#0292cd" stroke-width="3"/>
      </svg>
      <span>lemlem@amorrowventure.com</span>
    </li>
    <li class="contact__item">
      <svg class="contact__icon" viewBox="0 0 44 32" aria-hidden="true">
        <path d="M4 11 C4 3 40 3 40 11 L40 14 L31 14 L31 9 L13 9 L13 14 L4 14 Z" fill="#0292cd"/>
        <path d="M14 13 L30 13 L38 29 L6 29 Z" fill="#0292cd"/>
        <circle cx="22" cy="21" r="4.5" fill="#ffffff"/>
      </svg>
      <span>(215)483-2756</span>
    </li>
  </ul>
</div>
</body>
</html>
```